Updated flyer

we are a defence industry trainer and we are updating a course that has been running for a few years, so want a new look flyer. Please note that the flyer is A4 and we would like people to fill in the document online. Please add a tickbox for SME's free and add a call out box saying the course is NEW & UPDATED.

Industry/Entity Type

Defence

Font styles to use
Sans Serif
Other font styles liked:
• AVENIR

Colors
3176b5
01a88e
9bcb3b
fbed22
f37022

```html
<!DOCTYPE html>
<html lang="en">
<head>
<meta charset="utf-8">
<title>Defence, ITAR &amp; EAR Training Controls – Flyer</title>
<link href="https://fonts.googleapis.com/css2?family=Nunito+Sans:ital,wght@0,400;0,600;0,700;0,800;0,900;1,400;1,600&family=Archivo+Black&family=Roboto+Condensed:wght@300;400;700&display=swap" rel="stylesheet">
<style>
:root{
  --blue:#3176b5;
  --sky:#1f9ad6;
  --green:#1f8a3c;
  --teal:#01a88e;
  --lime:#9bcb3b;
  --yellow:#fbed22;
  --orange:#f37022;
  --red:#e02a1a;
  --ink:#1f5f9e;
  --pale:#dcecf8;
  --board-dark:#2a2a2a;
  --board-light:#9a9a9a;
}
*{box-sizing:border-box;margin:0;padding:0}
html,body{width:1200px;height:900px;overflow:hidden}
body{
  position:relative;
  font-family:"Nunito Sans",Arial,sans-serif;
  background:radial-gradient(ellipse at 50% 40%,var(--board-light) 0%,#5e5e5e 55%,var(--board-dark) 100%);
}
.board-label{
  position:absolute;font-family:"Archivo Black",Arial,sans-serif;color:var(--yellow);
  font-size:38px;letter-spacing:1px;
}
.board-note{
  position:absolute;font-family:"Nunito Sans",Arial,sans-serif;font-weight:900;
  color:var(--yellow);font-size:30px;
}
.page{
  position:absolute;top:63px;width:523px;height:742px;background:#fff;
  box-shadow:6px 8px 14px rgba(0,0,0,.55);overflow:hidden;
}
.page--one{left:57px}
.page--two{left:622px;height:737px}
.abs{position:absolute}

/* brand */
.brand{position:absolute;display:flex;align-items:center;gap:10px}
.brand__dot{border-radius:50%;background:var(--teal)}
.brand__name{color:var(--blue);font-weight:700;line-height:1}

/* page one */
.header-wash{left:0;top:0;width:523px;height:120px;background:linear-gradient(180deg,#e8f2fa,#fff)}
.badge{
  left:412px;top:16px;width:92px;height:92px;border-radius:50%;background:var(--green);
  border:4px solid #fff;box-shadow:0 2px 6px rgba(0,0,0,.35);
  display:flex;flex-direction:column;align-items:center;justify-content:center;transform:rotate(18deg);
}
.badge__new{color:var(--red);background:#fff;border-radius:4px;padding:0 6px;font-weight:900;font-size:22px;line-height:1.1}
.badge__updated{color:#fff;font-weight:800;font-size:14px;margin-top:2px}
.title-band{
  left:0;top:127px;width:492px;height:52px;background:var(--green);color:#fff;padding:5px 0 0 28px;
  border-bottom:4px solid var(--lime);
}
.title-band__main{font-weight:800;font-size:22px;line-height:1.1}
.title-band__sub{font-style:italic;font-size:17px;line-height:1.1}
.select-tab{left:0;top:220px;width:180px;height:16px;background:var(--green);color:#fff;font-size:11px;padding:1px 0 0 28px;letter-spacing:.3px}
.locations{left:0;top:240px;list-style:none}
.locations li{
  width:133px;height:31px;margin-bottom:2px;display:flex;align-items:center;gap:8px;padding-left:10px;
  background:linear-gradient(90deg,#d4e8f7,#f4f9fd);color:var(--sky);font-size:20px;font-weight:600;
}
.locations li::before{content:"";width:12px;height:12px;border-radius:50%;background:var(--red);box-shadow:0 0 0 2px #fff}
.map-area{left:200px;top:200px;width:275px;height:235px;background:linear-gradient(160deg,#3aaeea,#1a80c6)}
.route-layer{left:0;top:0;width:523px;height:742px}
.date-box{
  background:linear-gradient(180deg,#f2552c,#c81e0f);color:#fff;border-radius:4px;text-align:center;
  box-shadow:2px 3px 4px rgba(0,0,0,.35);font-weight:700;padding-top:5px;
}
.date-box__city{font-size:12px;letter-spacing:.5px}
.date-box__dates{font-size:12px;margin-top:6px}
.intro{left:18px;top:442px;width:288px;color:var(--ink);font-size:11.5px;line-height:1.17;text-align:justify}
.intro p+p{margin-top:10px}
.price{left:315px;top:437px;width:208px;height:57px;background:var(--green);border-radius:22px 0 0 0;color:#fff;text-align:center;padding-top:14px}
.price__amount{font-size:17px;font-weight:600;line-height:1}
.price__note{font-size:11px}
.sme{left:315px;top:494px;width:208px;height:125px;background:linear-gradient(180deg,#fff,var(--pale));text-align:center;padding-top:18px}
.sme__who{color:var(--red);font-size:13px}
.sme__free{color:var(--red);font-size:15px;font-weight:800;margin-top:2px}
.sme__by{color:var(--ink);font-size:11px;margin-top:6px;line-height:1.2}
.quotes{left:22px;top:625px;width:296px;list-style:none;color:var(--green);font-style:italic;font-size:10.6px;line-height:15px;white-space:nowrap}
.photo{left:323px;top:622px;width:200px;height:85px;background:linear-gradient(135deg,#e9eef3,#b7c7d6 60%,#7b8ea3)}
.footer{left:0;top:717px;width:523px;height:25px;background:linear-gradient(90deg,#cfe5f5,#eef6fc);color:var(--ink);font-size:10.5px;padding:6px 0 0 22px;white-space:nowrap}

/* page two */
.head-band{left:170px;top:27px;width:353px;height:36px;background:var(--green);color:#fff;text-align:center;border-bottom:3px solid var(--lime);padding-top:1px}
.head-band__main{font-weight:800;font-size:15px;line-height:1.15}
.head-band__sub{font-style:italic;font-size:12.5px;line-height:1}
.scene-wash{left:228px;top:68px;width:295px;height:395px;background:radial-gradient(circle at 60% 55%,#dfe9f1 0%,#eef4f8 45%,#fff 80%)}
.content-list{left:18px;top:80px;width:395px;list-style:none;font-size:10.8px;line-height:12.95px;font-weight:600;white-space:nowrap}
.content-list li:nth-child(odd){color:var(--sky)}
.content-list li:nth-child(even){color:var(--green)}
.content-list li::before{content:"•"}
.course-tag{left:418px;top:85px;width:105px;background:var(--orange);color:#fff;text-align:center;padding:6px 4px 7px;font-family:"Roboto Condensed","Arial Narrow",sans-serif}
.course-tag__days{font-size:19px;font-weight:300;line-height:1.25}
.course-tag__course{font-size:26px;font-weight:700;line-height:1.2}
.course-tag__content{font-size:19px;font-weight:300;line-height:1.25}
.register-tag{left:418px;top:180px;width:105px;height:62px;background:var(--sky);color:#fff;font-family:"Roboto Condensed","Arial Narrow",sans-serif;font-size:12.5px;text-align:center;line-height:1.35;padding-top:6px}
.register-bar{left:0;top:467px;width:523px;height:14px;background:var(--green);color:#fff;font-size:10.5px;padding-left:22px;line-height:14px}
.register-bar b{font-weight:800}
.form-table{position:absolute;border-collapse:collapse;font-size:10px;color:var(--green);border:2px solid var(--sky)}
.form-table th{background:var(--sky);color:#fff;text-align:left;font-weight:700;padding:0 5px;height:12px}
.form-table th span{font-weight:400}
.form-table td{border:1px solid var(--sky);padding:0 5px;height:12px;line-height:11px;white-space:nowrap}
.details{left:15px;top:490px;width:250px}
.locations-form{left:278px;top:490px;width:230px}
.payment{left:15px;top:592px;width:250px}
.small-print{position:absolute;font-size:7px;line-height:8.5px;color:var(--ink)}
.small-print b{font-weight:800}
.surcharge{left:17px;top:702px;font-size:8px;font-weight:600;color:var(--sky);white-space:nowrap}
.submit{left:340px;top:603px;width:112px;height:24px;border-radius:12px;background:var(--red);color:#fff;font-size:9.5px;text-align:center;line-height:10px;padding-top:2px}
.office{left:280px;top:632px;width:228px;border:2px solid var(--green);border-radius:8px 8px 0 0;overflow:hidden;font-size:10px}
.office__head{background:var(--green);color:#fff;font-weight:800;padding:0 5px;height:13px;line-height:13px}
.office__row{color:var(--red);border-top:1px solid var(--green);padding:0 5px;height:15px;line-height:15px;font-weight:600}
.annot{position:absolute;left:0;top:0;width:1200px;height:900px;pointer-events:none}
</style>
</head>
<body>

<div class="board-label" style="left:255px;top:8px">PAGE 1</div>
<div class="board-label" style="left:804px;top:8px">PAGE 2</div>

<!-- PAGE ONE -->
<section class="page page--one">
  <div class="abs header-wash"></div>
  <div class="brand" style="left:22px;top:30px">
    <span class="brand__dot" style="width:62px;height:62px"></span>
    <span class="brand__name" style="font-size:31px;width:240px">Trade Compliance Centre</span>
  </div>
  <div class="abs badge"><span class="badge__new">NEW</span><span class="badge__updated">UPDATED</span></div>

  <div class="abs title-band">
    <div class="title-band__main">Defence, ITAR &amp; EAR Training Controls</div>
    <div class="title-band__sub">from a non-U.S. Perspective Training</div>
  </div>

  <div class="abs select-tab">SELECT YOUR <b>LOCATION</b>:</div>
  <ul class="abs locations">
    <li>Adelaide</li><li>Brisbane</li><li>Canberra</li><li>Melbourne</li><li>Sydney</li>
  </ul>

  <div class="abs map-area" role="img" aria-label="Map of Australia marking the five course cities"></div>

  <svg class="abs route-layer" viewBox="0 0 523 742" aria-hidden="true">
    <g fill="#e02a1a" stroke="#b71a0c" stroke-width="1">
      <polygon points="330,239 342,239 405,345 412,356 398,352"/>
      <polygon points="238,295 252,292 398,365 404,375 392,372"/>
      <polygon points="455,243 466,243 452,292 446,300 444,290"/>
      <polygon points="262,337 268,350 355,352 366,352 355,345"/>
      <polygon points="320,400 322,410 385,382 392,378 383,378"/>
    </g>
  </svg>

  <div class="abs date-box" style="left:263px;top:189px;width:135px;height:50px"><div class="date-box__city">SYDNEY</div><div class="date-box__dates">18 &amp; 19 March</div></div>
  <div class="abs date-box" style="left:405px;top:195px;width:100px;height:48px"><div class="date-box__city">BRISBANE</div><div class="date-box__dates">16 &amp; 17 March</div></div>
  <div class="abs date-box" style="left:165px;top:245px;width:135px;height:50px"><div class="date-box__city">CANBERRA</div><div class="date-box__dates">20 &amp; 23 March</div></div>
  <div class="abs date-box" style="left:143px;top:308px;width:125px;height:45px"><div class="date-box__city">ADELAIDE</div><div class="date-box__dates">26 &amp; 27 March</div></div>
  <div class="abs date-box" style="left:195px;top:375px;width:130px;height:48px"><div class="date-box__city">MELBOURNE</div><div class="date-box__dates">24 &amp; 25 March</div></div>

  <div class="abs intro">
    <p><b>U.S. Export Controls</b> are some of the most complex and stringent in the world. The U.S. Government regulates the transfer of U.S. origin goods and technical data throughout the world, with the intent of preventing unauthorised transfer of technology and know-how. These controls extend world-wide and can impact anyone dealing in U.S. controlled goods or technology.</p>
    <p>This two-day comprehensive course will give applicants a greater understanding of U.S. Export Controls from a non-U.S. perspective in practical and relevant terms.</p>
  </div>

  <div class="abs price"><div class="price__amount">$1295.00 AUD</div><div class="price__note">per person inc GST</div></div>
  <div class="abs sme">
    <div class="sme__who">Small to Medium Enterprises</div>
    <div class="sme__free">FREE OF CHARGE</div>
    <div class="sme__by">Subsidised by: (DSGO)<br>Defence Skills Growth Office</div>
  </div>

  <ul class="abs quotes">
    <li>“Excellent structure and style of presentation.”</li>
    <li>“Excellent...best U.S export controls training I have attended.”</li>
    <li>“Practical workshops were fantastic.”</li>
    <li>“Excellent presenter and coordination.”</li>
    <li>“Very informative, well presented course.”</li>
  </ul>
  <div class="abs photo" role="img" aria-label="Photo of smiling course attendees in business attire"></div>

  <div class="abs footer">For more information, please contact TCC on +61 (0)7 5550 0142 or info@tradecompliance.example</div>
</section>

<!-- PAGE TWO -->
<section class="page page--two">
  <div class="abs header-wash" style="height:70px"></div>
  <div class="abs scene-wash" role="img" aria-label="Faint photo of business people walking through a glass office"></div>
  <div class="brand" style="left:20px;top:20px">
    <span class="brand__dot" style="width:40px;height:40px"></span>
    <span class="brand__name" style="font-size:15px;width:100px">Trade Compliance Centre</span>
  </div>
  <div class="abs head-band">
    <div class="head-band__main">Defence, ITAR &amp; EAR Training Controls</div>
    <div class="head-band__sub">from a non-U.S. Perspective Training</div>
  </div>

  <ul class="abs content-list">
    <li>Export Control terms and conditions</li>
    <li>Export Control Reform and the impact to Australian industry</li>
    <li>Managing reclassifications</li>
    <li>Applying deminimis</li>
    <li>Understanding 600 Series &amp; limitations</li>
    <li>Understanding the Commerce Country List, Country Chart &amp; Country Groups</li>
    <li>Understanding deemed exports</li>
    <li>EAR General Prohibitions</li>
    <li>U.S. export controls jurisdictions</li>
    <li>Relevant legislation</li>
    <li>Understand U.S. authorisations</li>
    <li>Sub-licensing options &amp; requirements</li>
    <li>Applying U.S. exemptions</li>
    <li>Understanding re-exports &amp; how to obtain authorisation</li>
    <li>Australian export controls</li>
    <li>Australian / U.S. Trade Co-operation Treaty</li>
    <li>Dual &amp; third country national issues &amp; exemptions</li>
    <li>Developing a compliance framework</li>
    <li>Clound Computing &amp; other technical issues</li>
    <li>Managing multi-jurisdictions</li>
    <li>Identifying the best authorisations to use</li>
    <li>Recordk-keeping &amp; administrative requirements</li>
    <li>Understanding FMS</li>
    <li>Creating a monitoring &amp; self-assessment process</li>
    <li>Managing violations</li>
    <li>Non-compliance &amp; fines</li>
    <li>Case Studies</li>
    <li>Best practice principles</li>
    <li>Strategic planning</li>
  </ul>

  <div class="abs course-tag">
    <div class="course-tag__days">2 DAY</div>
    <div class="course-tag__course">COURSE</div>
    <div class="course-tag__content">CONTENT</div>
  </div>
  <div class="abs register-tag">REGISTER ONLINE<br>OR FILL IN<br>THE FORM BELOW</div>

  <div class="abs register-bar"><b>REGISTER NOW</b> &nbsp;FILL IN THE FORM BELOW</div>

  <table class="form-table details">
    <tr><th colspan="2">Details</th></tr>
    <tr><td style="width:80px">Name</td><td></td></tr>
    <tr><td>Company</td><td></td></tr>
    <tr><td>Address</td><td></td></tr>
    <tr><td>Mobile no.</td><td></td></tr>
    <tr><td>Email</td><td></td></tr>
    <tr><td>Dietary needs</td><td></td></tr>
  </table>

  <table class="form-table locations-form">
    <tr><th colspan="3">Course location<span>: (please check)</span></th></tr>
    <tr><td style="width:60px;border-right:0">Brisbane</td><td style="border-left:0">16 &amp; 17 &nbsp;March</td><td style="width:24px"></td></tr>
    <tr><td style="border-right:0">Sydney</td><td style="border-left:0">18 &amp; 19 &nbsp;March</td><td></td></tr>
    <tr><td style="border-right:0">Canberra</td><td style="border-left:0">20 &amp; 23 &nbsp;March</td><td></td></tr>
    <tr><td style="border-right:0">Melbourne</td><td style="border-left:0">24 &amp; 25 &nbsp;March</td><td></td></tr>
    <tr><td style="border-right:0">Adelaide</td><td style="border-left:0">26 &amp; 27 &nbsp;March</td><td></td></tr>
  </table>

  <p class="small-print" style="left:280px;top:570px;width:235px"><b>Cancellation Policy:</b> Cancellations incur a 20% administration fee. No cancellations permitted within 30 days of training commencing. If a registered attendee is unable to attend, a replacement attendee is allowed.</p>

  <table class="form-table payment">
    <tr><th colspan="4">Payment method<span>: (please check one)</span></th></tr>
    <tr><td style="width:110px">Invoice</td><td colspan="3">&nbsp; FREE of Charge (SME)</td></tr>
    <tr><td>Credit card*</td><td colspan="3"></td></tr>
    <tr><td>Card type: Globecard</td><td></td><td>Voyacard</td><td>Amcard</td></tr>
    <tr><td>Card name</td><td colspan="3"></td></tr>
    <tr><td>Card number</td><td colspan="3"></td></tr>
    <tr><td>Expiry date</td><td colspan="3"></td></tr>
    <tr><td>Cardholder email</td><td colspan="3"></td></tr>
  </table>
  <p class="small-print surcharge">Credit card payments incur a 2.5% surcharge. Amcard incurs 3%</p>

  <div class="abs submit">or click here to submit<br>your registration</div>

  <div class="abs office">
    <div class="office__head">OFFICE USE ONLY:</div>
    <div class="office__row">Confirmation sent</div>
    <div class="office__row">Invoice no.</div>
    <div class="office__row">Contact person</div>
    <div class="office__row">Paid</div>
  </div>

  <div class="abs footer" style="top:712px;text-align:center;padding-left:0">Alternatively you can Register online @ tradecompliance.example/events or fax to +61 (0)7 5550 0199</div>
</section>

<svg class="annot" viewBox="0 0 1200 900" aria-hidden="true">
  <defs>
    <linearGradient id="arrowFill" x1="0" y1="1" x2="0" y2="0">
      <stop offset="0" stop-color="#f37022"/>
      <stop offset="1" stop-color="#fbed22"/>
    </linearGradient>
  </defs>
  <path d="M150 852 C40 760 70 560 228 488" fill="none" stroke="url(#arrowFill)" stroke-width="10" stroke-linecap="round"/>
  <polygon points="244,470 206,478 226,505" fill="#fbed22"/>
  <path d="M1052 856 C1120 820 1130 760 1090 718" fill="none" stroke="url(#arrowFill)" stroke-width="10" stroke-linecap="round"/>
  <polygon points="1078,700 1070,734 1102,724" fill="#fbed22"/>
</svg>

<div class="board-note" style="left:173px;top:840px">Buttons to show Places &amp; Dates</div>
<div class="board-note" style="left:780px;top:840px">Button to submit</div>

</body>
</html>
```